We need a new design/function for our reusable Sandwich paper bag

1. We need a designer who can help us create a design and improve the functionality of our paper lunch bag (image attached) and create "a new design for our new sandwich paper bag".

We would like to see designs for people age +18 ( working men, collage). The sandwich paper bag design should have a zipper (colored zipper is available) at the top, the sandwich bag dimension will be 8.5 x7.75x 1.5 in

2. The designer must also design a simple package cover for the sandwich bag

The feature of the material that will be used in manufacturing the sandwich paper bag: It combines the advantages of paper, film, and weaving. It is thinner than paper, but it is tough and tear resistant, texture and touch. Unique, waterproof, anti-fouling and weather-resistant, environmentally friendly and recyclable, has been widely used in textile

Target Market(s)

USA, Canada

Colors

Designer to choose colors to be used in the design.

Requirements
Must have
• Design for the sandwich paper bag
• Package design for the sandwich bag
• The designer must remember that there should be a zipper at the top of the bag
• Kindly find a suitable and small place to put our logo in it, besides the bag
Nice to have
• Try to design something that covers the crumpled paper bag look or appear it in a fashion way
• We appreciate if we can see an improvement in the functionality of the paper sandwich bag, not only the design. We need a new idea on how people will use this bag
Should not have
• Please don't use food images in your design

```html
<!DOCTYPE html>
<html lang="en">
<head>
<meta charset="utf-8">
<title>Eat. Travel. Repeat. — Sandwich Bag</title>
<link rel="stylesheet" href="https://fonts.googleapis.com/css2?family=Open+Sans:wght@700;800&family=Lato:wght@400;700&display=swap">
<style>
  :root {
    --kraft: #c9a277;
    --kraft-light: #ead6bd;
    --red: #e4595a;
    --red-dark: #b8393d;
    --navy: #1f2a5c;
    --paper-white: #ece8e4;
    --zip: #f2c21b;
    --ink-light: #f6dedd;
  }
  * { margin: 0; padding: 0; box-sizing: border-box; }
  html, body { width: 1200px; height: 901px; overflow: hidden; background: var(--kraft); }
  .bag-face {
    position: relative; width: 1200px; height: 901px; overflow: hidden;
    background: radial-gradient(ellipse at 60% 40%, #d1ab80 0%, var(--kraft) 70%);
    font-family: "Lato", sans-serif;
  }
  .zip-band { position: absolute; left: 0; top: 0; width: 1200px; height: 16px; background: var(--zip); }
  .shapes { position: absolute; inset: 0; }
  .halftone { position: absolute; }
  .halftone--left {
    left: 0; top: 16px; width: 290px; height: 420px;
    background: radial-gradient(ellipse at 30% 40%, rgba(240,228,212,.55) 0%, rgba(240,228,212,0) 70%);
  }
  .halftone--right {
    left: 880px; top: 320px; width: 320px; height: 390px;
    background: radial-gradient(ellipse at 60% 60%, rgba(240,228,212,.55) 0%, rgba(240,228,212,0) 70%);
  }
  .brand {
    position: absolute; left: 0; width: 1200px; top: 92px; text-align: center;
    font-family: "Open Sans", sans-serif; font-weight: 800; color: var(--navy);
    font-size: 38px; line-height: 44px; letter-spacing: .5px;
  }
  .brand-rule { position: absolute; left: 554px; top: 200px; width: 90px; height: 3px; background: var(--red); }
  .slogan {
    position: absolute; font-family: "Open Sans", sans-serif; font-weight: 800;
    color: var(--paper-white); line-height: 1; white-space: nowrap;
  }
  .slogan--eat { left: 366px; top: 208px; font-size: 212px; letter-spacing: -6px; }
  .slogan--travel { left: 371px; top: 395px; font-size: 98px; letter-spacing: -2px; }
  .slogan--repeat { left: 376px; top: 482px; font-size: 98px; letter-spacing: -2px; }
  .emblem {
    position: absolute; left: 405px; top: 580px; width: 280px; height: 272px;
    border-radius: 46% 46% 22% 22%;
    background: radial-gradient(ellipse at 50% 55%, rgba(184,57,61,.55) 0%, rgba(184,57,61,.15) 75%);
  }
  .contact { position: absolute; left: 78px; top: 670px; list-style: none; }
  .contact__item { display: flex; align-items: center; gap: 12px; height: 28px; margin-bottom: 10px; color: var(--ink-light); font-size: 11px; line-height: 12px; }
  .contact__icon { width: 22px; height: 22px; flex: none; }
  .contact__rule { position: absolute; left: 78px; top: 831px; width: 190px; height: 1px; background: var(--ink-light); opacity: .8; }
  .social { position: absolute; left: 78px; top: 843px; display: flex; align-items: center; gap: 10px; }
  .social__dot { width: 24px; height: 24px; border-radius: 50%; background: #1a1a1a; }
  .social__tag { font-size: 9px; font-weight: 700; color: var(--ink-light); margin-left: 2px; }
  .feature { position: absolute; top: 760px; width: 202px; color: var(--ink-light); }
  .feature--yummy { left: 719px; }
  .feature--fresh { left: 929px; }
  .feature__title { font-family: "Open Sans", sans-serif; font-weight: 800; font-size: 20px; line-height: 22px; margin-bottom: 6px; }
  .feature__text { font-size: 8px; line-height: 10px; text-transform: uppercase; text-align: justify; }
</style>
</head>
<body>
<main class="bag-face">
  <div class="zip-band"></div>

  <div class="halftone halftone--left" role="img" aria-label="Halftone dot pattern in pale cream"></div>
  <div class="halftone halftone--right" role="img" aria-label="Halftone dot pattern in pale cream"></div>

  <svg class="shapes" width="1200" height="901" viewBox="0 0 1200 901" aria-hidden="true">
    <polygon fill="var(--red)" points="0,605 372,258 780,252 838,360 830,470 820,570 728,690 728,711 1200,711 1200,901 0,901"/>
    <line x1="671" y1="852" x2="1200" y2="852" stroke="var(--red-dark)" stroke-width="5"/>
  </svg>

  <h1 class="brand">COMPANY<br>NAME</h1>
  <div class="brand-rule"></div>

  <div class="slogan slogan--eat">EAT.</div>
  <div class="slogan slogan--travel">TRAVEL.</div>
  <div class="slogan slogan--repeat">REPEAT.</div>

  <div class="emblem" role="img" aria-label="Line illustration of a burger topped with a city skyline"></div>

  <ul class="contact">
    <li class="contact__item">
      <svg class="contact__icon" viewBox="0 0 22 22"><circle cx="11" cy="11" r="11" fill="var(--ink-light)"/><path d="M7 8c0-1 1-2 4-2s4 1 4 2v1h-2V8H9v1H7zM8 10h6l1 5H7z" fill="var(--red)"/></svg>
      <span>+1 555 014 2300<br>+1 555 014 2300</span>
    </li>
    <li class="contact__item">
      <svg class="contact__icon" viewBox="0 0 22 22"><circle cx="11" cy="11" r="11" fill="var(--ink-light)"/><rect x="6" y="7.5" width="10" height="7" fill="var(--red)"/><path d="M6 7.5l5 4 5-4" stroke="var(--ink-light)" fill="none"/></svg>
      <span>hello@lunchloop.co</span>
    </li>
    <li class="contact__item">
      <svg class="contact__icon" viewBox="0 0 22 22"><circle cx="11" cy="11" r="11" fill="var(--ink-light)"/><path d="M11 17s-4-4.5-4-7.5a4 4 0 0 1 8 0C15 12.5 11 17 11 17z" fill="var(--red)"/><circle cx="11" cy="9.5" r="1.5" fill="var(--ink-light)"/></svg>
      <span>88 Harbor Lane, Portland, USA</span>
    </li>
    <li class="contact__item">
      <svg class="contact__icon" viewBox="0 0 22 22"><circle cx="11" cy="11" r="11" fill="var(--ink-light)"/><g fill="none" stroke="var(--red)" stroke-width="1.2"><circle cx="11" cy="11" r="5"/><ellipse cx="11" cy="11" rx="2.2" ry="5"/><path d="M6 11h10"/></g></svg>
      <span>www.lunchloop.co</span>
    </li>
  </ul>
  <div class="contact__rule"></div>

  <div class="social">
    <span class="social__dot"></span>
    <span class="social__dot"></span>
    <span class="social__dot"></span>
    <span class="social__tag">#COMPANY NAME</span>
  </div>

  <section class="feature feature--yummy">
    <h2 class="feature__title">YUMMY</h2>
    <p class="feature__text">Packed with bold flavour for busy days on the go, this bag keeps your lunch ready wherever the road or the office takes you.</p>
  </section>
  <section class="feature feature--fresh">
    <h2 class="feature__title">FRESH</h2>
    <p class="feature__text">Tough, waterproof and fully recyclable, the zip closure locks in freshness so every bite tastes just as good as the moment it was made.</p>
  </section>
</main>
</body>
</html>
```